Children’s entertainer/balloon artist Website Home Page and custom landing page

I need a home page design for the home page of a children and family entertainer/balloon twister’s website. I also need a custom landing page for family theatre shows performed by the same entertainer.
It will be a Wordpress website and I need the final artwork in a layer Photoshop file with all the layers clearly named and labeled.

Target Market(s)

The site visitors are mainly mums, aged between early 20’s and late 30’s. Other visitors will included companies for Christmas functions, and event organisers for corporate functions.

Industry/Entity Type

Entertainment

Number of Pages Required

2 page

Font styles to use
Sans Serif

Colors
34a6d7
f37122

Requirements
Must have
• Layout
• I have included a wireframe for the home page layout and the custom landing page for your reference. This is a guide only and I welcome your interpretation with the rough layout provided.
• This website needs to look good on all devices as it will be fully responsive.
• It needs to include a footer area on the page, that has social media and a call to action area included.
• Colours
• The main colours for the site is:
• orange (call to action colour)
• ff6800
• blue/turquoise
• 42abc3
• Pictures
• I have included images of the entertainer/balloon artist for you to use/take inspiration from.
• These images will be included on the website. I want to show lots of people having fun.
• I would like to have elements of the logo used in isolation across the website
• i.e. the octopus figure to be included in the footer or the bird element to be included in the testimonial slider etc.
• Elements to include
• Note: use the images of the entertainer in the boxes on the home page (balloon shows, balloon twisting, balloon workshops, theatre shows (the three little balloon pigs on his head)
Nice to have
Should not have
• Element to avoid
• Stock imagery of balloon sculptures - use images provided.

```html
<!DOCTYPE html>
<html lang="en">
<head>
<meta charset="utf-8">
<title>Benny Marlowe – Children's Entertainer</title>
<link href="https://fonts.googleapis.com/css2?family=Nunito:wght@700;800;900&family=Open+Sans:wght@400;600;700&display=swap" rel="stylesheet">
<style>
  :root {
    --sky: #34a6d7;
    --sky-deep: #1f86c2;
    --sky-light: #7fd0f0;
    --orange: #f37122;
    --orange-bright: #ff6800;
    --teal: #42abc3;
    --yellow: #ffe23a;
    --pink: #e8407a;
    --ink: #333333;
    --muted: #6b6b6b;
    --dark-btn: #2b2b2b;
    --white: #ffffff;
    --footer-bg: #f4f6f8;
  }
  * { box-sizing: border-box; margin: 0; padding: 0; }
  html, body { width: 870px; height: 1200px; overflow: hidden; }
  body { font-family: "Open Sans", Arial, sans-serif; color: var(--ink); background: var(--white); }

  .page {
    position: relative; width: 870px; height: 1200px; overflow: hidden;
    background: radial-gradient(ellipse at 50% 0%, var(--sky-light) 0%, var(--sky) 45%, var(--sky-deep) 100%);
  }

  /* Header */
  .brand {
    position: absolute; left: 14px; top: 18px; display: flex; align-items: center; gap: 8px;
    font-family: "Nunito", Arial, sans-serif; font-weight: 900; font-size: 22px; color: var(--white);
  }
  .brand-dot { width: 34px; height: 34px; border-radius: 50%; background: var(--orange); }
  .main-nav {
    position: absolute; left: 255px; top: 74px; width: 586px; height: 36px;
    background: var(--white); border-radius: 6px 6px 0 0;
    display: flex; align-items: center; justify-content: space-around; padding: 0 10px;
  }
  .main-nav a {
    font-size: 12px; font-weight: 600; color: var(--ink); text-decoration: none; padding: 6px 12px; border-radius: 4px;
  }
  .main-nav a.is-active { background: var(--orange-bright); color: var(--white); }

  /* Hero */
  .hero {
    position: absolute; left: 78px; top: 110px; width: 763px; height: 300px;
    background: linear-gradient(160deg, #1e3f8a 0%, #3a5fc0 40%, #e86a3a 75%, #f2b544 100%);
  }
  .hero-name {
    position: absolute; left: 0; right: 0; bottom: 28px; text-align: center;
    font-family: "Nunito", Arial, sans-serif; font-weight: 800; font-size: 36px; color: var(--white);
  }

  /* Content panel */
  .content {
    position: absolute; left: 78px; top: 410px; width: 763px; height: 300px; background: var(--white);
  }
  .intro { position: absolute; left: 18px; top: 20px; width: 455px; }
  .section-title {
    font-family: "Nunito", Arial, sans-serif; font-weight: 800; font-size: 20px; color: var(--orange);
  }
  .testimonial { display: flex; gap: 14px; margin-top: 12px; }
  .quote-mark {
    font-family: "Nunito", Arial, sans-serif; font-weight: 900; font-size: 64px; line-height: 0.8; color: var(--sky);
  }
  .testimonial p { font-size: 10px; line-height: 1.55; color: var(--muted); }
  .testimonial cite { display: block; margin-top: 6px; font-style: normal; font-size: 10px; color: var(--ink); }
  .welcome { margin-top: 24px; }
  .welcome .section-title { color: var(--sky); }
  .welcome p { font-size: 10px; line-height: 1.55; color: var(--muted); margin-top: 8px; }

  .sidebar { position: absolute; right: 0; top: 25px; width: 268px; }
  .book-box {
    height: 102px; background: var(--orange-bright); text-align: center; padding-top: 20px;
  }
  .book-box h3 {
    font-family: "Nunito", Arial, sans-serif; font-weight: 800; font-size: 20px; color: var(--white); letter-spacing: 0.5px;
  }
  .btn {
    display: inline-block; font-size: 10px; font-weight: 700; letter-spacing: 0.5px;
    color: var(--white); text-decoration: none; padding: 7px 16px; border-radius: 3px;
  }
  .btn-blue { background: var(--sky); margin-top: 12px; }
  .btn-orange { background: var(--orange-bright); }
  .btn-dark { background: var(--dark-btn); border-radius: 12px; padding: 6px 14px; font-size: 9px; }

  .profile-box {
    position: relative; height: 168px; margin-top: 5px;
    background: linear-gradient(135deg, var(--sky-deep) 0%, var(--sky) 55%, #f0a35a 100%);
  }
  .profile-box .profile-name {
    position: absolute; left: 14px; top: 58px; width: 160px;
    font-family: "Nunito", Arial, sans-serif; font-weight: 800; font-size: 26px; line-height: 1.05; color: var(--white);
  }
  .profile-box .btn { position: absolute; left: 14px; bottom: 14px; }

  /* Service cards */
  .services {
    position: absolute; left: 85px; top: 740px; width: 751px; display: flex; gap: 17px;
  }
  .service-card {
    width: 175px; height: 195px; border-radius: 6px; text-align: center; padding-top: 16px;
  }
  .service-card h4 {
    font-family: "Nunito", Arial, sans-serif; font-weight: 800; font-size: 19px; line-height: 1.05; color: var(--white); height: 42px;
  }
  .service-card .service-photo {
    width: 92px; height: 92px; border-radius: 50%; margin: 4px auto 12px; border: 3px solid var(--white);
  }
  .card-blue { background: var(--sky); }
  .card-teal { background: var(--teal); }
  .card-orange { background: var(--orange-bright); }
  .card-yellow { background: var(--yellow); }
  .card-yellow h4 { color: var(--pink); }
  .photo-cool { background: radial-gradient(circle at 50% 40%, #f4c7a1 0%, #5b8fd6 70%); }
  .photo-warm { background: radial-gradient(circle at 50% 40%, #f4c7a1 0%, #e35b46 70%); }
  .photo-pink { background: radial-gradient(circle at 50% 40%, #f4c7a1 0%, #f28bb5 70%); }

  /* Footer */
  .site-footer {
    position: absolute; left: 0; top: 960px; width: 870px; height: 240px; background: var(--footer-bg);
  }
  .footer-cols { display: flex; gap: 40px; padding: 26px 60px 0 78px; }
  .footer-col { width: 165px; }
  .footer-col h5 {
    font-family: "Nunito", Arial, sans-serif; font-weight: 800; font-size: 13px; color: var(--sky); margin-bottom: 8px;
  }
  .footer-col li { list-style: none; font-size: 10px; line-height: 1.8; color: var(--muted); }
  .footer-col .btn { margin-top: 8px; }
  .social li { display: flex; justify-content: space-between; align-items: center; width: 120px; }
  .social-dot { width: 14px; height: 14px; border-radius: 50%; background: var(--sky); }
  .copyright {
    position: absolute; left: 0; right: 0; bottom: 16px; text-align: center; font-size: 9px; color: var(--muted);
    border-top: 1px solid #e1e5e9; padding-top: 12px; margin: 0 78px;
  }
</style>
</head>
<body>
<div class="page">

  <header>
    <div class="brand"><span class="brand-dot"></span>Balloon Benny</div>
    <nav class="main-nav">
      <a href="#" class="is-active">Home</a>
      <a href="#">Balloon Shows</a>
      <a href="#">Balloon Twisting</a>
      <a href="#">Theatre</a>
      <a href="#">Reviews</a>
      <a href="#">Contact</a>
    </nav>
  </header>

  <section class="hero" role="img" aria-label="Photo of the entertainer surrounded by colourful balloon sculptures">
    <h1 class="hero-name">Benny Marlowe</h1>
  </section>

  <main class="content">
    <div class="intro">
      <h2 class="section-title">Testimonials</h2>
      <div class="testimonial">
        <span class="quote-mark">“</span>
        <div>
          <p>Benny was the highlight of our party. The children laughed from start to finish, every guest went home with a balloon, and the grown‑ups were just as amazed by his tricks. We will certainly book him again for next year.</p>
          <cite>Gordon Mills, Company Name</cite>
        </div>
      </div>
      <div class="welcome">
        <h2 class="section-title">Welcome to Benny Marlowe</h2>
        <p>Benny is a children and family entertainer who brings fun, colour and laughter to birthday parties, school fairs and festive events. His lively balloon shows mix comedy, magic and audience games, so every child gets a chance to join in and shine.</p>
        <p>From twisting balloon animals at busy events to running hands‑on workshops and theatre shows, Benny tailors each booking to your guests. Get in touch today to check dates and find the perfect show for your celebration.</p>
      </div>
    </div>

    <aside class="sidebar">
      <div class="book-box">
        <h3>BOOK MY SHOW</h3>
        <a href="#" class="btn btn-blue">CONTACT THE ENTERTAINER</a>
      </div>
      <div class="profile-box" role="img" aria-label="Photo of the entertainer holding a balloon sculpture">
        <span class="profile-name">Benny Marlowe</span>
        <a href="#" class="btn btn-orange">CLICK HERE</a>
      </div>
    </aside>
  </main>

  <section class="services">
    <article class="service-card card-blue">
      <h4>Balloon<br>Shows</h4>
      <div class="service-photo photo-cool" role="img" aria-label="Entertainer performing a balloon show"></div>
      <a href="#" class="btn btn-dark">LEARN MORE</a>
    </article>
    <article class="service-card card-teal">
      <h4>Balloon<br>Twisting</h4>
      <div class="service-photo photo-cool" role="img" aria-label="Entertainer twisting balloon animals"></div>
      <a href="#" class="btn btn-dark">LEARN MORE</a>
    </article>
    <article class="service-card card-orange">
      <h4>Balloon<br>Workshops</h4>
      <div class="service-photo photo-warm" role="img" aria-label="Entertainer leading a balloon workshop"></div>
      <a href="#" class="btn btn-dark">LEARN MORE</a>
    </article>
    <article class="service-card card-yellow">
      <h4>Theatre<br>Shows</h4>
      <div class="service-photo photo-pink" role="img" aria-label="Entertainer with three balloon pigs on his head"></div>
      <a href="#" class="btn btn-dark">LEARN MORE</a>
    </article>
  </section>

  <footer class="site-footer">
    <div class="footer-cols">
      <div class="footer-col">
        <h5>Menu Links</h5>
        <ul>
          <li>Home</li><li>Balloon Shows</li><li>Balloon Twisting</li><li>Theatre</li><li>Reviews</li><li>Contact</li>
        </ul>
      </div>
      <div class="footer-col">
        <h5>About Links</h5>
        <ul><li>Terms Of Use</li><li>Privacy Policy</li></ul>
        <a href="#" class="btn btn-orange">CONTACT THE ENTERTAINER</a>
      </div>
      <div class="footer-col">
        <h5>Contact Us</h5>
        <ul>
          <li>Balloon Benny Ltd</li><li>14 Meadow Lane</li><li>Littleford</li><li>LF4 2BN</li>
          <li>Telephone: 01234 567 890</li><li>Email: hello@balloonbenny.example</li>
        </ul>
      </div>
      <div class="footer-col">
        <h5>Connect With Us</h5>
        <ul class="social">
          <li>Friendsite <span class="social-dot"></span></li>
          <li>Chirper <span class="social-dot"></span></li>
          <li>WorkLink <span class="social-dot"></span></li>
        </ul>
      </div>
    </div>
    <p class="copyright">© 2020 Company Name | All Rights Reserved</p>
  </footer>

</div>
</body>
</html>
```